Basisdesign Buch-/E-Book-Cover für Haldmoor-Krimis
Zielgruppe
Ich schreibe Krimis, Thriller, Kriminalstories, Krimiparodien.
Meine Zielgruppe sind deutschsprachige Krimi-Leser.
Aufgabenstellung
Ich benötige ein Basisdesign für Buchcover (Höhe 2.343, Breite 1.518 Pixel – Druckfalter, eBooks). Alle Bücher haben mit Crime zu tun, aber in verschiedenen Unter-Genres: Klassischer Kriminalroman, Thriller, Fantasy Thriller, Kurzgeschichten, Krimi-Parodien.
Ich benötige, quasi als Marke, dafür ein gleichbleibendes grafisches Element, z. B. einen Sockel im unteren Coverbereich, der den Autorennamen „Jonas Haldmoor“ und das jeweilige Unter-Genre enthält. Unter-Genres sind: Krimi, Thriller, Fantasy-Thriller, Kurzgeschichten und Krimi-Parodie. Das alles sollte auch noch im Format der Lesoria-Bücherlisten wie „Kunden kauften auch“ halbwegs lesbar sein.
Ein bisschen mörderisch und blutig sind alle Varianten.
Nachdem die Bandbreite vom Thriller bis zur Parodie reicht, sollte der gleichbleibende Markenbereich eine entsprechende grafische Bandbreite aufweisen, dabei aber die Grundmelodie Crime nicht aus den Augen verlieren.
Im oberen Bereich stelle ich mir Grafiken oder Hintergrundfotos vor, die für jedes Buch individuell gestaltet werden müssten, was jedoch über das Basisdesign hinausgeht. Die Wahl der Schriftart für Titel (bislang 11 – 25 Zeichen inkl. Leerzeichen) und allfällige Untertitel (im Umfang von maximal 30 Zeichen), sollte zu denen im Sockel passen.

```html
<!DOCTYPE html>
<html lang="de">
<head>
<meta charset="utf-8">
<title>Serena Moretti – Die Endlosbahn</title>
<link rel="stylesheet" href="https://fonts.googleapis.com/css2?family=Oswald:wght@600&family=Crimson+Text:ital@0;1&display=swap">
<style>
  :root {
    --title-cyan: #2ed0fb;
    --edge-cyan: #27c6ee;
    --badge-cyan: #35d3fb;
    --badge-ring: #b9effd;
    --sky-deep: #0f2666;
    --sky-mid: #1c4fa6;
    --sky-light: #3f8dd8;
    --cloud: #e4ecf4;
    --city: #d6ad62;
    --city-shade: #b98a44;
    --river: #3aa394;
    --river-deep: #2b7ec2;
    --paper: #ffffff;
  }
  html, body {
    margin: 0;
    padding: 0;
    width: 768px;
    height: 1200px;
    overflow: hidden;
    background: #ffffff;
  }
  .cover {
    position: relative;
    width: 768px;
    height: 1200px;
    overflow: hidden;
  }
  .cover-scene {
    position: absolute;
    left: 0;
    top: 0;
    width: 741px;
    height: 1200px;
    background: linear-gradient(180deg,
      var(--sky-deep) 0%,
      var(--sky-mid) 34%,
      var(--sky-light) 55%,
      var(--cloud) 67%,
      var(--cloud) 72%,
      var(--city) 76%,
      var(--city-shade) 82%,
      var(--river) 86%,
      var(--river-deep) 100%);
  }
  .edge-stripe {
    position: absolute;
    left: 741px;
    top: 0;
    width: 27px;
    height: 1200px;
    background: var(--edge-cyan);
  }
  .title-block {
    position: absolute;
    left: 0;
    top: 0;
    width: 741px;
    height: 700px;
  }
  .title-line {
    font-family: "Oswald", "Arial Narrow", sans-serif;
    font-weight: 600;
    fill: var(--title-cyan);
  }
  .genre {
    position: absolute;
    left: 0;
    width: 741px;
    top: 580px;
    margin: 0;
    text-align: center;
    font-family: "Crimson Text", Georgia, serif;
    font-style: italic;
    font-weight: 400;
    font-size: 46px;
    line-height: 1.2;
    letter-spacing: 1px;
    color: var(--paper);
  }
  .author {
    position: absolute;
    left: 0;
    width: 741px;
    top: 1068px;
    margin: 0;
    text-align: center;
    font-family: "Crimson Text", Georgia, serif;
    font-weight: 400;
    font-size: 70px;
    line-height: 1;
    color: var(--paper);
  }
  .publisher-badge {
    position: absolute;
    left: 622px;
    top: 787px;
    width: 146px;
    height: 146px;
  }
</style>
</head>
<body>
  <main class="cover">
    <div class="cover-scene" role="img" aria-label="Foto: blauer Himmel mit Wolken über einer alten Brücke und einem Fluss in einer italienischen Stadt, oben rote Blutspritzer"></div>
    <div class="edge-stripe"></div>

    <svg class="title-block" viewBox="0 0 741 700" aria-label="Serena Moretti – Die Endlosbahn">
      <text class="title-line" x="111" y="246" font-size="184" textLength="519" lengthAdjust="spacingAndGlyphs">SERENA</text>
      <text class="title-line" x="50" y="457" font-size="184" textLength="630" lengthAdjust="spacingAndGlyphs">MORETTI</text>
      <text class="title-line" x="163" y="551" font-size="60" textLength="421" lengthAdjust="spacingAndGlyphs">DIE ENDLOSBAHN</text>
    </svg>

    <p class="genre">Fantasy-Thriller</p>

    <svg class="publisher-badge" viewBox="0 0 146 146" aria-hidden="true">
      <circle cx="73" cy="73" r="72" fill="var(--badge-ring)"/>
      <circle cx="73" cy="73" r="66" fill="var(--badge-cyan)"/>
    </svg>

    <p class="author">Jonas Haldmoor</p>
  </main>
</body>
</html>
```